BOLD & MINIMALIST DESIGN NEEDED

We want a very bold but minimalistic business card design that is impactful and utilizes both sides of the business card. Our current logo is included for your use.

We want bold fonts and good use of negative space. We don't want the logo to overpower the design.

Target Market(s)

Professionals who are building new commercial buildings.

Industry/Entity Type

Construction

Contact Information for Business Card

Name, Title, email, office phone, cell phone, website

Font styles to use
Serif
Sans Serif

Requirements
Must have
• Bold design!

```html
<!DOCTYPE html>
<html lang="en">
<head>
<meta charset="utf-8">
<title>Stonefield Business Card</title>
<link href="https://fonts.googleapis.com/css2?family=Montserrat:wght@800&family=Open+Sans:wght@400;600&display=swap" rel="stylesheet">
<style>
  :root {
    --stage: #ececec;
    --paper: #ffffff;
    --ink: #111111;
    --lime: #7dc242;
    --lime-soft: #a6d874;
    --muted: #6b6b6b;
  }
  * { box-sizing: border-box; margin: 0; padding: 0; }
  html, body { width: 1200px; height: 900px; overflow: hidden; }
  body {
    background: var(--stage);
    font-family: "Open Sans", Arial, sans-serif;
    position: relative;
  }
  .card {
    position: absolute;
    width: 560px;
    height: 320px;
    border-radius: 26px;
    overflow: hidden;
    box-shadow: 0 14px 30px rgba(0,0,0,0.18);
  }
  .card--front { left: 80px; top: 100px; background: var(--paper); }
  .card--back  { left: 560px; top: 480px; background: var(--ink); }

  .brand {
    display: flex;
    align-items: center;
    gap: 10px;
    font-family: "Montserrat", Arial, sans-serif;
    font-weight: 800;
    letter-spacing: 0.5px;
    line-height: 1;
  }
  .brand__mark { display: block; background: var(--lime); }

  .card--front .brand {
    position: absolute; left: 36px; top: 34px;
    font-size: 34px; color: var(--ink);
  }
  .card--front .brand__mark { width: 14px; height: 14px; }

  .person { position: absolute; left: 36px; top: 90px; }
  .person__name {
    font-weight: 600; font-size: 19px; color: var(--lime);
    text-transform: uppercase; letter-spacing: 0.3px;
  }
  .person__title { font-size: 13px; color: var(--muted); margin-top: 1px; }

  .address {
    position: absolute; left: 36px; top: 150px;
    font-size: 13px; color: var(--muted); line-height: 1.45;
    font-style: normal;
  }
  .contacts {
    position: absolute; left: 36px; top: 198px;
    list-style: none; font-size: 13px; color: var(--muted); line-height: 1.5;
  }
  .contacts li { display: flex; align-items: center; gap: 6px; }
  .contacts svg { width: 11px; height: 11px; fill: var(--lime); flex: none; }

  .sweep { position: absolute; left: 0; bottom: 0; width: 560px; height: 320px; }

  .card--back .brand {
    position: absolute; left: 50%; top: 50%;
    transform: translate(-50%, -50%);
    font-size: 46px; color: var(--paper);
  }
  .card--back .brand__mark { width: 18px; height: 18px; }
</style>
</head>
<body>

<section class="card card--front" aria-label="Business card front">
  <svg class="sweep" viewBox="0 0 560 320" aria-hidden="true">
    <path d="M0 250 C 90 255 170 285 215 320 L 0 320 Z" fill="var(--ink)"/>
    <rect x="380" y="150" width="140" height="140" fill="var(--lime)"/>
    <rect x="380" y="150" width="140" height="30" fill="var(--lime-soft)"/>
  </svg>

  <div class="brand"><span class="brand__mark"></span>STONEFIELD</div>

  <div class="person">
    <p class="person__name">Marcus Hale</p>
    <p class="person__title">Managing Director</p>
  </div>

  <address class="address">
    Your Address<br>
    City, State, Zip 0000
  </address>

  <ul class="contacts">
    <li>
      <svg viewBox="0 0 24 24" aria-hidden="true"><path d="M6.6 10.8a15 15 0 0 0 6.6 6.6l2.2-2.2a1 1 0 0 1 1-.25 11.4 11.4 0 0 0 3.6.57 1 1 0 0 1 1 1V20a1 1 0 0 1-1 1A17 17 0 0 1 3 4a1 1 0 0 1 1-1h3.5a1 1 0 0 1 1 1c0 1.25.2 2.45.57 3.57a1 1 0 0 1-.25 1z"/></svg>
      044-555 0100 22
    </li>
    <li>
      <svg viewBox="0 0 24 24" aria-hidden="true"><path d="M2 5h20v14H2z M4 7v.5l8 5 8-5V7l-8 5z" fill-rule="evenodd"/></svg>
      hello@stonefield.co
    </li>
    <li>
      <svg viewBox="0 0 24 24" aria-hidden="true"><circle cx="12" cy="12" r="10"/></svg>
      www.stonefield.co
    </li>
  </ul>
</section>

<section class="card card--back" aria-label="Business card back">
  <div class="brand"><span class="brand__mark"></span>STONEFIELD</div>
</section>

</body>
</html>
```